Box packaging design for Black Hair Shampoo
Brand Name: LunaVeko
Product Name: Black Hair Shampoo
Target Market: Low-mid end consumers in Indonesia
Box Size: 12.5 cm (Height) × 9.3 cm (Length) × 7.5 cm (Width)
Net Content: 25 ml × 10 sachets

Design Requirements:
Color Scheme:
Primary: Black (background)
Secondary: Green (accent color)
Additional Colors: Subtle complementary colors (e.g., white, gold, or soft neutrals) may be used to enhance readability and visual appeal, but the design should remain cohesive and not overpower the primary black and green theme.

Must Include:
1. Product Slogan:
"LunaVeko Black Hair Shampoo – Where rich tones find strong roots."

2. Product Description:
"Deep, Long-Lasting Black Color with Nourishing Care
Achieve rich, vibrant black hair in just 5 minutes with LunaVeko Black Hair Shampoo, a premium formula designed to deliver intense color while nourishing and protecting your hair. Enriched with natural extracts like Morus Nigra Fruit (antioxidant-rich, shine-enhancing properties), Polygonum Multiflorum Root (strengthening and revitalizing hair), and Ganoderma Atrum Mushroom (deep hydration and repair benefits), this shampoo deeply conditions your hair, leaving it soft, shiny, and full of life. Experience a deep, fade-resistant black color that stays vibrant and bold for up to 4 weeks, while your hair feels nourished, soft, and radiant."

3. Shampoo Color Ingredients:
Aqua, Sodium Laureth Sulfate, Propylene Glycol, Ethanolamine, Morus Nigra Fruit Extract, Polygonum Multiflorum Root Extract, Ganoderma Atrum (Mushroom) Extract, p-Phenylenediamine, Hydroxyethylcellulose, Resorcinol, Carbomer, Angelica Archangelica Root Extract, 2,4-Diaminophenoxyethanol HCl, Sodium Erythorbate, Phenyl Methyl Pyrazolone, Chrysanthemum Indicum Flower Extract, Lonicera Japonica (Honeysuckle) Flower Extract, Rheum Palmatum Root Extract, Chrysanthellum Indicum Extract, Sophora Flavescens Root Extract, Prunus Speciosa Flower Extract, Punica Granatum Fruit Extract

4. Developer Ingredients:
Aqua, Hydrogen Peroxide, Cetearyl Alcohol, Sodium Laureth Sulfate, Disodium Phosphate, Etidronic Acid, Parfum

5. Instructions:
Include the instructions exactly as shown in the provided picture.

6. Free Extra Item:
Mention the inclusion of plastic gloves as a free extra item.

7. Distributor Information:
Include the following at the bottom of the box:
"Distributed by: PT. Sorang MEKARJAYA INDONESIA
Jl. Raya Pandanwuni 14 Karangsedo Malang - Indonesia"

8. Barcode Placement:
Leave space for the barcode on the box design.
Suggest a suitable placement for the barcode (e.g., bottom right or left corner of the back panel).

Additional Notes:
-Logo Placement:
I do not yet have a logo for LunaVeko. Please leave space for the logo on the box design and suggest a suitable placement for it.
- The design should reflect a low-mid end product with a premium feel.
- Ensure the text is clear and legible against the black background.
- Use green accents strategically to highlight key information (e.g., brand name, slogan).
- Consider incorporating subtle visuals or patterns that evoke natural ingredients or vibrant hair color.
Updates

1. Brand Overview
Brand Name: LunaVeko
Tagline: "Vibrant Color, Healthier Hair."
Mission: To provide a natural, effective, and convenient solution for achieving deep, long-lasting black hair color while nourishing and protecting hair.
Target Audience:
Men and women aged 18–45.
Individuals looking for a natural alternative to chemical hair dyes.
Busy professionals who want quick, salon-quality results at home.

2. Product Description
Achieve rich, vibrant black hair in just 5 minutes with LunaVeko Black Hair Shampoo! Our premium formula is designed to deliver intense color while deeply nourishing and protecting your hair.
Enriched with 11 natural extracts—including Black Mulberry (for shine and UV protection), Fo-Ti Root (for strength and growth), and Reishi Mushroom (for hydration and repair)—this shampoo:
✅ Enhances black hair color for a bold, fade-resistant finish.
✅ Strengthens and nourishes hair, reducing breakage and split ends.
✅ Protects against environmental damage and soothes the scalp.
Experience soft, shiny, and radiant hair that stays vibrant for up to 4 weeks. With LunaVeko, you’re not just coloring your hair—you’re giving it the care it deserves!"

3. Key Selling Points
11 Natural Extracts: Black Mulberry, Fo-Ti Root, Reishi Mushroom, and more for holistic hair care.
Quick Application: Visible results in just 5 minutes.
Multi-Benefit Formula: Combines color enhancement with deep conditioning, scalp care, and protection.
Safe and Natural: Free from harsh chemicals like ammonia, PPD, and parabens.

4. Competitive Edge
Natural Ingredients: Unlike competitors that rely on synthetic dyes, LunaVeko uses 11 natural extracts for safer, healthier hair care.
Quick Results: Delivers vibrant color in just 5 minutes, making it ideal for busy lifestyles.

5. Color Palette: Feel free to use any color (max 4 color)

```html
<!DOCTYPE html>
<html lang="en">
<head>
<meta charset="utf-8">
<title>LunaVeko Black Hair Shampoo – Box Dieline</title>
<link rel="stylesheet" href="https://fonts.googleapis.com/css2?family=Cinzel:wght@700&family=Oswald:wght@300;500&display=swap">
<style>
  :root {
    --paper: #ffffff;
    --board: #0b0b0a;
    --panel: #121210;
    --panel-glow: #232321;
    --cap: #2b2b2b;
    --inset: #0a0a09;
    --fold: #e8e8e8;
    --green: #63d823;
    --white: #ffffff;
    --icon-tone: #6f6f6f;
  }
  * { margin: 0; padding: 0; box-sizing: border-box; }
  html, body { width: 1200px; height: 1200px; overflow: hidden; background: var(--paper); }
  .canvas { position: relative; width: 1200px; height: 1200px; }
  .dieline { position: absolute; inset: 0; }
  .text { position: absolute; color: var(--green); font-family: "Oswald", sans-serif; text-transform: uppercase; }

  .brand-flap { left: 330px; width: 293px; top: 312px; text-align: center; font-family: "Cinzel", serif; font-weight: 700; font-size: 34px; letter-spacing: 1px; text-transform: none; }
  .brand-front { left: 330px; width: 293px; top: 510px; text-align: center; font-family: "Cinzel", serif; font-weight: 700; font-size: 34px; letter-spacing: 2px; }
  .slogan { left: 340px; width: 273px; top: 604px; text-align: center; font-weight: 500; font-size: 19px; line-height: 28px; letter-spacing: -0.2px; }

  .instructions-title { left: 173px; top: 462px; font-weight: 500; font-size: 15px; }
  .step-art { position: absolute; left: 121px; width: 55px; height: 58px; border: 2px solid var(--white); border-radius: 4px; background: linear-gradient(160deg, #f2f2f2, #bdbdbd); }
  .step-num { position: absolute; left: 2px; top: -1px; font-family: "Oswald", sans-serif; font-size: 8px; color: #000; }
  .step-text { left: 186px; width: 140px; font-weight: 500; font-size: 7.6px; line-height: 12.2px; }

  .ingredients { left: 638px; width: 200px; font-weight: 300; font-size: 8px; line-height: 13.5px; text-align: justify; }
  .ingredients p { margin: 0; }

  .description { left: 886px; top: 491px; width: 238px; font-weight: 300; font-size: 11.3px; line-height: 16.9px; text-align: justify; letter-spacing: -0.2px; }
  .free-item { left: 874px; top: 744px; width: 70px; text-align: center; color: var(--white); font-weight: 500; font-size: 6.6px; line-height: 10px; }
</style>
</head>
<body>
<main class="canvas">
  <svg class="dieline" width="1200" height="1200" viewBox="0 0 1200 1200" aria-hidden="false">
    <defs>
      <radialGradient id="panelGlow" cx="50%" cy="50%" r="70%">
        <stop offset="0" stop-color="var(--panel-glow)"/>
        <stop offset="1" stop-color="var(--panel)"/>
      </radialGradient>
    </defs>

    <!-- top tuck flap -->
    <path class="tuck-cap" d="M330 213 V200 Q330 174 360 174 H593 Q623 174 623 200 V213 Z" fill="var(--cap)"/>
    <!-- top dust flaps -->
    <path class="dust-flap" d="M93 450 V340 Q93 316 120 316 H310 Q330 316 330 340 V450 Z" fill="var(--board)"/>
    <path class="dust-flap" d="M624 450 V336 Q624 316 645 316 H838 Q860 316 860 340 V450 Z" fill="var(--board)"/>
    <!-- glue flap -->
    <path class="glue-flap" d="M93 450 H75 Q46 450 46 480 V815 Q46 845 75 845 H93 Z" fill="var(--board)"/>
    <!-- bottom flaps -->
    <path class="bottom-flap" d="M93 845 H330 L210 914 V977 H93 Z" fill="var(--board)"/>
    <path class="bottom-flap" d="M330 845 H623 V1026 H560 Q551 1026 551 1017 V961 H403 V1017 Q403 1026 394 1026 H330 Z" fill="var(--board)"/>
    <path class="bottom-flap" d="M624 845 H860 V977 H745 V914 Z" fill="var(--board)"/>
    <path class="bottom-flap" d="M861 845 H1153 L1080 961 V1012 Q1080 1026 1066 1026 H948 Q934 1026 934 1012 V961 Z" fill="var(--board)"/>

    <g role="img" aria-label="Subtle grey swirl ornament pattern on black">
      <rect x="330" y="213" width="293" height="237" fill="url(#panelGlow)"/>
      <rect x="93" y="450" width="237" height="395" fill="url(#panelGlow)"/>
      <rect x="330" y="450" width="293" height="395" fill="url(#panelGlow)"/>
      <rect x="624" y="450" width="236" height="395" fill="url(#panelGlow)"/>
      <rect x="861" y="450" width="292" height="395" fill="url(#panelGlow)"/>
      <rect x="330" y="845" width="293" height="116" fill="url(#panelGlow)" opacity="0.8"/>
    </g>

    <!-- text insets -->
    <rect class="inset" x="632" y="466" width="220" height="374" fill="var(--inset)"/>
    <rect class="inset" x="873" y="474" width="268" height="256" fill="var(--inset)"/>

    <!-- barcode space -->
    <rect class="barcode-space" x="956" y="748" width="171" height="69" fill="var(--white)"/>

    <!-- fold lines -->
    <g stroke="var(--fold)" stroke-width="1" fill="none">
      <line x1="330" y1="213" x2="623" y2="213"/>
      <line x1="93" y1="450" x2="1153" y2="450"/>
      <line x1="93" y1="845" x2="1153" y2="845"/>
      <line x1="93" y1="450" x2="93" y2="845"/>
      <line x1="330" y1="316" x2="330" y2="1026"/>
      <line x1="623.5" y1="316" x2="623.5" y2="1026"/>
      <line x1="860.5" y1="450" x2="860.5" y2="845"/>
    </g>
  </svg>

  <div class="text brand-flap">LunaVeko</div>
  <div class="text brand-front">LUNAVEKO</div>
  <div class="text slogan">LunaVeko Black Hair<br>Shampoo – Where rich tones<br>find strong roots</div>

  <div class="text instructions-title">Instructions:</div>

  <div class="step-art" style="top:496px" role="img" aria-label="Illustration: man with grey hair holding a comb"><span class="step-num">1</span></div>
  <div class="text step-text" style="top:512px">Please be sure the hair<br>is dry before use</div>

  <div class="step-art" style="top:562px" role="img" aria-label="Illustration: hands putting on black gloves"><span class="step-num">2</span></div>
  <div class="text step-text" style="top:585px">Wear the gloves</div>

  <div class="step-art" style="top:628px" role="img" aria-label="Illustration: gloved hand squeezing a sachet"><span class="step-num">3</span></div>
  <div class="text step-text" style="top:645px">Squeeze out the cream mix<br>evenly and apply on hair</div>

  <div class="step-art" style="top:693px" role="img" aria-label="Illustration: man massaging foam into hair"><span class="step-num">4</span></div>
  <div class="text step-text" style="top:691px">Massage hair slightly unit the<br>cream spread evenly on hair.<br>Keep the cream on hair for 5-10 mins.<br>If the hair is more,<br>please use 2-3 sachets for on time.</div>

  <div class="step-art" style="top:760px" role="img" aria-label="Illustration: man blow drying black hair"><span class="step-num">5</span></div>
  <div class="text step-text" style="top:783px">Wash and blow dry hair</div>

  <div class="text ingredients" style="top:486px">
    <p>Shampoo color ingredients:</p>
    <p>Aqua, Sodium Laureth Sulfate, Propylene Glycol, Ethanolamine, Morus Nigra Fruit Extract, Polygonum Multiflorum Root Extract, Ganoderma Atrum (Mushroom) Extract, p-Phenylenediamine, Hydroxyethylcellulose, Resorcinol, Carbomer, Angelica Archangelica Root Extract, 2,4-Diaminophenoxyethanol HCl, Sodium Erythorbate, Phenyl Methyl Pyrazolone, Chrysanthemum Indicum Flower Extract, Lonicera Japonica (Honeysuckle) Flower Extract, Rheum Palmatum Root Extract, Chrysanthellum Indicum Extract, Sophora Flavescens Root Extract, Prunus Speciosa Flower Extract, Punica Granatum Fruit Extract</p>
  </div>
  <div class="text ingredients" style="top:688px">
    <p>Developer ingredients:</p>
    <p>Aqua, Hydrogen Peroxide, Cetearyl Alcohol, Sodium Laureth Sulfate, Disodium Phosphate, Etidronic Acid, Parfum</p>
  </div>
  <div class="text ingredients" style="top:762px">
    <p>Distributor information:</p>
    <p>Include the following at the bottom of the box:</p>
    <p>"Distributed by: PT. Sorang MEKARJAYA INDONESIA</p>
    <p>Jl. Raya Pandanwuni 14 Karangsedo Malang - Indonesia"</p>
  </div>

  <div class="text description">"Deep, long-lasting black color with nourishing care achieve rich, vibrant black hair in just 5 minutes with LunaVeko Black Hair Shampoo, a premium formula designed to deliver intense color while nourishing and protecting your hair. Enriched with natural extracts like Morus Nigra Fruit (antioxidant-rich, shine-enhancing properties), Polygonum Multiflorum Root (strengthening and revitalizing hair), and Ganoderma Atrum Mushroom (deep hydration and repair benefits), this shampoo deeply conditions your hair, leaving it soft, shiny, and full of life. Experience a deep, fade-resistant black color that stays vibrant and bold for up to 4 weeks, while your hair feels nourished, soft, and radiant."</div>

  <div class="text free-item">Free extra item:<br>Plastic gloves</div>
  <svg class="gloves-icon" style="position:absolute;left:874px;top:765px" width="70" height="55" viewBox="0 0 70 55" role="img" aria-label="Illustration: pair of white plastic gloves">
    <rect x="0" y="0" width="70" height="55" rx="6" fill="var(--icon-tone)" opacity="0.5"/>
  </svg>
</main>
</body>
</html>
```